Business Cards Needed For Veterinary Business

Looking for a business card design for a veterinary blood bank. We would like it to be clean and professional on appearance but still warm and inviting. We would like to utilize our logo and similar coloring. We will use our phone number, email, website, employee name, employee title.

We do not want a bunch of animated animal photos but do not need the style to be as clinical as a laboratory or human medical procedure office.

We are looking for some creative ideas to choose from so that we can generate a standout professional business card for our management team to utilize.

Target Market(s)

professionals

Industry/Entity Type

veterinary

Contact Information for Business Card

employee name, employee title, phone number, website URL, email

Font styles to use
Sans Serif

Colors
0054AA
0677BA
7BADD7
CADEEF
E8F1F8
EB3D1F
EC4F4E
F09395
F8D3D4
FCEDEE

Requirements
Nice to have
• creative design
Should not have
• animated photos

```html
<!DOCTYPE html>
<html lang="en">
<head>
<meta charset="utf-8">
<title>Northline Animal Blood Bank – Business Card</title>
<link href="https://fonts.googleapis.com/css2?family=Montserrat:wght@400;500;700;800&display=swap" rel="stylesheet">
<style>
  :root {
    --brand-red: #EC1C2B;
    --brand-red-soft: #EC4F4E;
    --brand-blue: #0054AA;
    --brand-blue-mid: #0677BA;
    --paper: #ffffff;
    --backdrop: #E8F1F8;
    --divider: #F09395;
  }
  * { box-sizing: border-box; margin: 0; padding: 0; }
  html, body {
    width: 1200px; height: 886px; overflow: hidden;
    background: var(--backdrop);
    font-family: "Montserrat", sans-serif;
  }
  .canvas { position: relative; width: 1200px; height: 886px; }

  .card {
    position: absolute;
    width: 560px; height: 320px;
    border-radius: 4px;
    overflow: hidden;
    box-shadow: 0 6px 18px rgba(0, 40, 90, 0.18);
  }

  /* Front side */
  .card--front { left: 50px; top: 100px; background: var(--brand-red); }
  .card--front .brand {
    position: absolute; inset: 0;
    display: flex; align-items: center; justify-content: center; gap: 18px;
  }
  .brand__dot {
    width: 54px; height: 54px; border-radius: 50%;
    background: var(--paper);
    flex: none;
  }
  .brand__name {
    color: var(--paper);
    font-weight: 700;
    line-height: 1.05;
  }
  .card--front .brand__name { font-size: 34px; }
  .brand__name small { display: block; font-size: 0.5em; letter-spacing: 0.06em; font-weight: 700; }

  /* Back side */
  .card--back { left: 590px; top: 466px; background: var(--paper); }
  .card--back .swoosh { position: absolute; left: 0; top: 0; width: 560px; height: 320px; }
  .card--back .brand {
    position: absolute; left: 40px; top: 92px;
    display: flex; align-items: center; gap: 12px;
  }
  .card--back .brand__dot { width: 34px; height: 34px; background: var(--brand-red); }
  .card--back .brand__name { color: var(--brand-red); font-size: 21px; }

  .divider {
    position: absolute; left: 276px; top: 58px;
    width: 1px; height: 120px; background: var(--divider);
  }
  .contact { position: absolute; left: 300px; top: 50px; }
  .contact__name { color: var(--brand-red); font-weight: 700; font-size: 20px; }
  .contact__title { color: var(--brand-blue); font-size: 13px; margin-top: 2px; }
  .contact__list { list-style: none; margin-top: 16px; }
  .contact__item {
    display: flex; align-items: center; gap: 9px;
    color: var(--brand-blue); font-size: 12px; margin-bottom: 7px;
    white-space: nowrap;
  }
  .contact__icon {
    width: 16px; height: 16px; border-radius: 4px;
    background: var(--brand-red);
    display: flex; align-items: center; justify-content: center;
    flex: none;
  }
  .contact__icon svg { width: 10px; height: 10px; }
</style>
</head>
<body>
<main class="canvas">

  <section class="card card--front" aria-label="Card front">
    <div class="brand">
      <span class="brand__dot"></span>
      <p class="brand__name">NORTHLINE<small>ANIMAL BLOOD BANK</small></p>
    </div>
  </section>

  <section class="card card--back" aria-label="Card back">
    <svg class="swoosh" viewBox="0 0 560 320" aria-hidden="true">
      <path d="M0 320 L0 292 C160 286 380 262 560 200 L560 320 Z" fill="var(--brand-red)"/>
      <path d="M120 280 C300 262 450 232 545 182 C450 240 300 270 120 280 Z" fill="var(--brand-blue)" stroke="var(--brand-blue)" stroke-width="3" stroke-linejoin="round"/>
    </svg>

    <div class="brand">
      <span class="brand__dot"></span>
      <p class="brand__name">NORTHLINE<small>ANIMAL BLOOD BANK</small></p>
    </div>

    <div class="divider"></div>

    <div class="contact">
      <p class="contact__name">Dana M. Holloway</p>
      <p class="contact__title">Founder and CEO</p>
      <ul class="contact__list">
        <li class="contact__item">
          <span class="contact__icon"><svg viewBox="0 0 10 10"><path d="M2 1 L4 1 L4.6 3 L3.4 3.8 C4 5 5 6 6.2 6.6 L7 5.4 L9 6 L9 8 C5 8.5 1.5 5 2 1 Z" fill="#fff"/></svg></span>
          (555) 204-7719
        </li>
        <li class="contact__item">
          <span class="contact__icon"><svg viewBox="0 0 10 10"><rect x="1" y="2.5" width="8" height="5.5" fill="none" stroke="#fff" stroke-width="1"/><path d="M1 2.5 L5 5.8 L9 2.5" fill="none" stroke="#fff" stroke-width="1"/></svg></span>
          dana@northlineabb.org
        </li>
        <li class="contact__item">
          <span class="contact__icon"><svg viewBox="0 0 10 10"><circle cx="5" cy="5" r="3.8" fill="none" stroke="#fff" stroke-width="1"/><path d="M1.2 5 H8.8 M5 1.2 C3 3.5 3 6.5 5 8.8 M5 1.2 C7 3.5 7 6.5 5 8.8" fill="none" stroke="#fff" stroke-width="0.8"/></svg></span>
          www.northlineabb.org
        </li>
      </ul>
    </div>
  </section>

</main>
</body>
</html>
```